Menubook for a 2star restaurant

Hey,
We are looking for a new menu for a 2 star restaurant in Belgium. They want a clean, abstract, with small light accents of gold, copper. The format will be 21 cm by 21 cm. and the booklet will have 4 printable sides inc front & back. Only the logo on the front. The wine list will be separate so it should not be included in the design. "Bites" - "voorgerechten" - "hoofdgerechten" & "nagerechten" must be copied.

Industry/Entity Type

Restaurant

Requirements
Must have
• Clean look
Nice to have
• touches of gold

```html
<!DOCTYPE html>
<html lang="nl">
<head>
<meta charset="utf-8">
<title>Solis – menukaart</title>
<link rel="stylesheet" href="https://fonts.googleapis.com/css2?family=Mulish:wght@400;700&display=swap">
<style>
  :root {
    --backdrop: #978a63;
    --paper: #ffffff;
    --ink: #1d1d1b;
    --gold: #c9a97a;
    --gold-soft: rgba(201, 169, 122, 0.28);
  }
  * { margin: 0; padding: 0; box-sizing: border-box; }
  html, body { width: 1200px; height: 1200px; overflow: hidden; }
  body {
    background: var(--backdrop);
    font-family: "Mulish", "Century Gothic", sans-serif;
    color: var(--ink);
    position: relative;
  }
  .spread {
    position: absolute;
    left: 208px;
    width: 784px;
    height: 392px;
    background: var(--paper);
    overflow: hidden;
  }
  .spread--outer { top: 194px; }
  .spread--inner { top: 614px; }

  .accent {
    position: absolute;
    background: radial-gradient(circle at var(--cx, 50%) var(--cy, 50%), var(--gold-soft) 0%, rgba(201,169,122,0.12) 45%, rgba(201,169,122,0) 72%);
  }
  .sparkle {
    position: absolute;
    background: radial-gradient(circle, rgba(201,169,122,0.35) 0%, rgba(201,169,122,0) 70%);
  }

  .frames { position: absolute; left: 0; top: 0; width: 784px; height: 392px; }

  .section-title {
    position: absolute;
    font-weight: 700;
    font-size: 7.5px;
    letter-spacing: 0.02em;
  }
  .dish {
    position: absolute;
    display: flex;
    justify-content: space-between;
    font-size: 7.6px;
    line-height: 1;
    white-space: nowrap;
  }
  .dish--small { font-size: 6.6px; }
  .note {
    position: absolute;
    display: flex;
    justify-content: space-between;
    font-size: 5.2px;
    line-height: 1;
    white-space: nowrap;
    padding-left: 4px;
  }
  .note .price { font-size: 6.4px; }
  .qty { font-size: 4.6px; }

  .brand {
    position: absolute;
    left: 510px;
    top: 178px;
    font-family: "Mulish", "Century Gothic", sans-serif;
    font-weight: 400;
    font-size: 26px;
    letter-spacing: 0.6em;
    color: var(--ink);
  }
</style>
</head>
<body>

<!-- Outer side: back and cover -->
<section class="spread spread--outer">
  <div class="accent" role="img" aria-label="Gouden zonnestralen ornament" style="left:293px;top:-60px;width:200px;height:160px;--cx:50%;--cy:30%;"></div>
  <div class="accent" role="img" aria-label="Gouden zonnestralen ornament" style="left:-40px;top:290px;width:140px;height:140px;--cx:30%;--cy:70%;"></div>
  <div class="accent" role="img" aria-label="Gouden zonnestralen ornament" style="left:685px;top:290px;width:140px;height:140px;--cx:75%;--cy:70%;"></div>

  <h2 class="section-title" style="left:105px;top:32px;">HOOFDGERECHTEN</h2>

  <div class="dish" style="left:105px;top:53px;width:183px;"><span>SPAGHETTI VONGOLE *</span><span>29</span></div>
  <div class="note" style="left:105px;top:62px;width:183px;"><span>bosui | piemento | zilte groenten</span></div>

  <div class="dish" style="left:105px;top:85px;width:183px;"><span>KABELJAUW RUG *</span><span>36</span></div>
  <div class="note" style="left:105px;top:94px;width:183px;"><span>limoen | kappertjes | mosselen | safraan</span></div>

  <div class="dish" style="left:105px;top:116px;width:183px;"><span>KALFSFILET *</span><span>46</span></div>
  <div class="note" style="left:103px;top:125px;width:183px;"><span>paarse bloemkool | girolle | groen asperge | daslook | pijpajuin</span></div>

  <div class="dish" style="left:105px;top:148px;width:183px;"><span>INSALATE DEL GIORNO</span></div>
  <div class="note" style="left:105px;top:156px;width:183px;"><span>vlees of vis</span><span class="price">40</span></div>
  <div class="note" style="left:105px;top:164px;width:183px;"><span>veggie</span><span class="price">33</span></div>

  <div class="dish" style="left:105px;top:187px;width:183px;"><span>GNOCCHI</span><span>29</span></div>
  <div class="note" style="left:106px;top:196px;width:183px;"><span>salie | spinazie | barlotto</span></div>

  <div class="dish" style="left:105px;top:219px;width:183px;"><span>GEPOCHEERD HOEVE EI</span><span>36</span></div>
  <div class="note" style="left:106px;top:228px;width:183px;"><span>girolle | daslook | groene asperges</span></div>

  <h2 class="section-title" style="left:105px;top:267px;">NAGERECHTEN</h2>

  <div class="dish" style="left:105px;top:293px;width:183px;"><span>ASSORTIMENT VAN 5 ITALIAANSE KAZEN</span><span>27</span></div>
  <div class="dish" style="left:105px;top:310px;width:183px;"><span>AMALFI CITROEN MET MERINGUE *</span><span>16</span></div>

  <div class="dish" style="left:107px;top:350px;width:181px;"><span>* MENU | 5 GANGEN</span><span>95</span></div>

  <div class="brand">solis</div>
</section>

<!-- Inner side: aperitivi and bites -->
<section class="spread spread--inner">
  <div class="accent" role="img" aria-label="Gouden halve zon ornament" style="left:680px;top:-50px;width:150px;height:150px;--cx:70%;--cy:30%;"></div>
  <div class="accent" role="img" aria-label="Gouden halve zon ornament" style="left:-50px;top:290px;width:150px;height:150px;--cx:30%;--cy:75%;"></div>
  <div class="sparkle" role="img" aria-label="Gouden sterretjes" style="left:37px;top:32px;width:31px;height:25px;"></div>
  <div class="sparkle" role="img" aria-label="Gouden sterretjes" style="left:739px;top:113px;width:20px;height:24px;"></div>
  <div class="sparkle" role="img" aria-label="Gouden sterretjes" style="left:422px;top:331px;width:26px;height:32px;"></div>

  <svg class="frames" viewBox="0 0 784 392" aria-hidden="true">
    <g fill="none" stroke="var(--gold)" stroke-width="0.8">
      <polygon points="67,60 323,60 330,67 330,326 323,333 67,333 61,326 61,67"/>
      <polygon points="64,63 326,63 329,66 329,328 326,331 64,331 61,328 61,66" transform="translate(0,-1)"/>
      <polygon points="459,60 715,60 722,67 722,326 715,333 459,333 453,326 453,67"/>
      <polygon points="456,63 718,63 721,66 721,328 718,331 456,331 453,328 453,66" transform="translate(0,-1)"/>
    </g>
  </svg>

  <h2 class="section-title" style="left:122px;top:113px;">APERITIVI</h2>
  <div class="dish dish--small" style="left:122px;top:137px;width:148px;"><span>CASA DEL MONTE</span><span>19</span></div>
  <div class="dish dish--small" style="left:122px;top:148px;width:148px;"><span>MAISON VERLAINE</span><span>21</span></div>
  <div class="dish dish--small" style="left:122px;top:170px;width:148px;"><span>ARANCIA SPRITZ</span><span>15</span></div>
  <div class="dish dish--small" style="left:122px;top:181px;width:148px;"><span>HUGO</span><span>15</span></div>
  <div class="dish dish--small" style="left:122px;top:204px;width:148px;"><span>GIN COSTA</span><span>18</span></div>
  <div class="dish dish--small" style="left:122px;top:215px;width:148px;"><span>COPPERVALE</span><span>19</span></div>
  <div class="dish dish--small" style="left:122px;top:226px;width:148px;"><span>LUMEN GIN (non alcoholisch)</span><span>19</span></div>
  <div class="dish dish--small" style="left:122px;top:248px;width:148px;"><span>NEGRONI SBAGLIATO</span><span>17</span></div>
  <div class="dish dish--small" style="left:122px;top:259px;width:148px;"><span>CLASSIC NEGRONI</span><span>19</span></div>
  <div class="dish dish--small" style="left:122px;top:270px;width:148px;"><span>AMARETTO SUNRISE</span><span>15</span></div>

  <h2 class="section-title" style="left:504px;top:91px;">BITES</h2>
  <div class="dish dish--small" style="left:504px;top:111px;width:169px;"><span>OESTER BELLE RIVE <span class="qty">(1st)</span></span><span>9</span></div>
  <div class="note" style="left:504px;top:119px;width:169px;"><span>jalapeño | komkommer | ajo blanco</span></div>
  <div class="note" style="left:504px;top:127px;width:169px;"><span>supplement kaviaar 5gr (+ €18)</span></div>
  <div class="dish dish--small" style="left:504px;top:142px;width:169px;"><span>Solis RISOTTO CROQUETTES <span class="qty">(2st)</span></span><span>9</span></div>
  <div class="dish dish--small" style="left:504px;top:158px;width:169px;"><span>CHARCUTERIE</span><span>15</span></div>
  <div class="note" style="left:504px;top:167px;width:169px;"><span>cornichon | olijven</span></div>
  <div class="dish dish--small" style="left:504px;top:181px;width:169px;"><span>KOUDE AMANDEL-KNOFLOOK ZUPPA</span><span>14</span></div>
  <div class="note" style="left:504px;top:190px;width:169px;"><span>fregola | kreeft</span></div>

  <h2 class="section-title" style="left:504px;top:226px;">VOORGERECHTEN</h2>
  <div class="dish dish--small" style="left:504px;top:251px;width:169px;"><span>ANTIPASTI &nbsp;*</span><span>35 p.p.</span></div>
  <div class="dish dish--small" style="left:504px;top:276px;width:169px;"><span>PIZZETTA AMARO</span></div>
  <div class="note" style="left:505px;top:285px;width:168px;"><span>met 1/2 kreeft | doperwt | basilicum | courgette</span><span class="price">37</span></div>
  <div class="note" style="left:505px;top:293px;width:168px;"><span>ook vegetarisch te bestellen</span><span class="price">32</span></div>
</section>

</body>
</html>
```